Lagoon Canopy NZ Product Catalogue

To redesign our suppliers catalogue and make it my own.
Verdmont is our supplier, although now I want a "Lagoon Canopy NZ" catalogue, with an updated look as well.

I have attached our logos, Verdmont catalogue and a few photos of completed work (which may need editing to look better).

Also pages I want to use from the catalogue (be similar to) are page numbers:
10 - 21 (products we sell)
It will also need a cover and contents page and a commercial enclosure page after the other products (with commercial 1 and 20130422_1 photos).

The first page as you open the catalogue I want the about us section of our website on there www.lagooncanopy.co.nz (two sections "what we offer" and "enclosure advantages")

If you need better photos or more information please contact me on:
tamsin@lagooncanopy.co.nz

Contact details: Toll Free 0508 SHELTERS (748 219) Email sales@lagooncanopy.co.nz

Industry/Entity Type

Construction

Colors

Designer to choose colors to be used in the design.

Requirements
Must have
• Must have double sided pages,
• With each different design to have two pages which open together.
• The standard sizing which is in the Verdmont Catalogue must be there.
• Designs are: Rivelle Horizon, Rivelle, Tormel, Quarry, Lisbet and Vale Shelters
• Must be printable and pdf sendable.
• Use "What we offer" and "Enclosure Advantages" to the first page customer opens to, maybe also a contents page.
• Also please add to the "enclosure advantages" bullet point list "Year-round average of 8 degree warmer water"
Nice to have
• Would be nice to have the custom sizing box as well on the designs asked for.
• Also a Commercial section after the rest of the designs using the "commercial 1" and "20130422_1" photos
• The more photos the better
• Be nice to be high resolution and I want to print it in a gloss finish.
• Also A4 size would be nice, but A5 will work also
Should not have
• Rivelle Horizon Neo and try and minimise the Verdmont branding

```html
<!DOCTYPE html>
<html lang="en">
<head>
<meta charset="utf-8">
<title>Lagoon Canopy NZ – Catalogue Pages</title>
<link rel="stylesheet" href="https://fonts.googleapis.com/css2?family=Arimo:wght@400;700&display=swap">
<style>
:root{
  --bg-top:#e4e4e6;
  --bg-bottom:#d2d2d5;
  --page:#ffffff;
  --blue:#1466d6;
  --blue-deep:#0b4cae;
  --blue-glass:rgba(18,92,205,.86);
  --green:#8cc63f;
  --ink:#2b2b2b;
  --muted:#6b6b6b;
  --row:#eef1f4;
}
*{box-sizing:border-box;margin:0;padding:0}
html,body{width:675px;height:1200px;overflow:hidden}
body{
  position:relative;
  font-family:"Arimo",Arial,sans-serif;
  color:var(--ink);
  background:linear-gradient(180deg,var(--bg-top),var(--bg-bottom));
}
.page,.spread{position:absolute;background:var(--page);overflow:hidden;box-shadow:0 1px 3px rgba(0,0,0,.18)}
.page{width:143px;height:202px;top:75px}
.spread{width:286px;height:205px}
.photo{position:absolute}

/* covers */
.cover .photo{inset:0;background:linear-gradient(180deg,#9fd4f6 0%,#d8ecf7 30%,#3c86c9 52%,#1ea1ee 70%,#0d76d3 100%)}
.brand{position:absolute;left:8px;top:9px;font-weight:700;font-size:9.5px;color:#fff;letter-spacing:.2px;display:flex;align-items:center;gap:3px}
.brand i{width:6px;height:6px;border-radius:50%;background:#fff;display:block}
.contact-box{position:absolute;right:0;bottom:18px;width:96px;height:40px;background:var(--blue-glass);color:#fff;padding:6px 7px;text-align:right}
.contact-box h3{font-size:6.5px;font-weight:700;margin-bottom:5px}
.contact-box p{font-size:2.8px;line-height:4.4px;text-align:left}
.title-panel{position:absolute;right:0;top:100px;width:110px;height:50px;background:var(--blue-glass);color:#fff;padding:10px 8px;text-align:right}
.title-panel h1{font-size:8px;font-weight:700;margin-bottom:3px}
.title-panel p{font-size:4.5px}

/* contents spread */
.contents{left:371px;top:75px;height:202px}
.half{position:absolute;top:0;width:143px;height:100%}
.half.left{left:0}.half.right{left:143px}
.bar{position:absolute;top:9px;height:11px;background:var(--blue);color:#fff;font-size:4.6px;line-height:11px;padding:0 5px}
.half.left .bar{left:0;width:70px}
.half.right .bar.head{right:0;width:70px;text-align:right}
.toc{position:absolute;left:5px;top:28px;width:130px;list-style:none}
.toc li{display:flex;justify-content:space-between;font-size:3.2px;border-bottom:.4px solid #ccc;padding:3px 0}
.toc-photo{left:6px;top:118px;width:70px;height:68px;background:linear-gradient(160deg,#6fc8f4,#1d8fe0 60%,#0c5fb8)}
.toc-side{position:absolute;left:80px;top:118px;width:58px;height:68px;background:var(--blue-deep)}
.folio-dark{position:absolute;bottom:3px;font-size:2.6px;color:var(--muted)}
.half.left .folio-dark{left:6px}.half.right .folio-dark{right:6px}
.offer-text{position:absolute;left:5px;top:24px;width:85px;font-size:2.6px;line-height:3.6px;color:var(--muted)}
.offer-text p+p{margin-top:2.5px}
.swim-photo{left:94px;top:24px;width:44px;height:18px;background:linear-gradient(90deg,#1b8fe0,#3db0f0)}
.bar.adv{left:4px;top:105px;width:80px}
.adv-box{position:absolute;left:4px;top:120px;width:135px;height:68px;background:var(--blue);color:#fff;padding:5px}
.adv-box ul{list-style:none;width:82px}
.adv-box li{font-size:2.6px;line-height:3.8px;padding-left:4px;position:relative}
.adv-box li::before{content:"";position:absolute;left:0;top:1.2px;width:1.5px;height:1.5px;background:#fff}
.adv-photo{right:4px;top:4px;width:48px;height:60px;background:linear-gradient(180deg,#bfe3f7,#2f9de6 60%,#0f6cc9)}

/* product spreads */
.product .hero{left:0;top:0;width:100%;height:153px}
.product .headline{position:absolute;right:0;top:58px;width:95px;height:78px;background:var(--blue-glass);color:#fff;padding:8px 6px 0}
.headline h2{font-size:9px;line-height:10px;font-weight:700;text-align:right;margin-bottom:4px}
.headline p{font-size:2.6px;line-height:3.5px}
.specs{position:absolute;left:4px;width:130px;border-collapse:collapse;font-size:2.5px;background:#fff}
.specs th{background:var(--green);color:#fff;font-weight:400;text-align:left;padding:1px 2px}
.specs td{padding:1px 2px;border-bottom:.3px solid #ddd}
.specs tr:nth-child(even) td{background:var(--row)}
.strip{position:absolute;left:0;top:153px;width:100%;height:52px;background:var(--blue);display:flex;align-items:flex-start;gap:4px;padding:5px 4px 0}
.strip .photo{position:relative}
.thumb{height:36px;flex:1;min-width:0}
.strip .frame{flex:2.1;display:flex;gap:4px;background:var(--blue-deep);padding:6px 4px 0;margin-top:-9px;height:50px}
.frame .thumb{height:36px}
.folio{position:absolute;bottom:3px;font-size:2.6px;color:#fff;display:flex;align-items:center;gap:2px}
.folio.l{left:6px}.folio.r{right:6px}
.folio b{width:2.5px;height:2.5px;background:#fff;display:block}

.t1{background:linear-gradient(180deg,#9ccbe9,#e6f1f7 40%,#3ea6ea 60%,#1b7fd8)}
.t2{background:linear-gradient(180deg,#cbe5f4,#6aa57a 45%,#2ba0e8 70%)}
.t3{background:linear-gradient(160deg,#dfeaf1,#9fa9a0 50%,#4b9bd1)}
.t4{background:linear-gradient(180deg,#b7d6ea,#7da56a 50%,#4aa0dc)}

.hero.horizon{background:linear-gradient(180deg,#d8ecf8 0%,#86b36e 30%,#2c7a3e 42%,#3aa9ec 55%,#1a89df 100%)}
.hero.rivelle{background:linear-gradient(180deg,#bfe1f6 0%,#e7f2f8 22%,#5e8a60 40%,#32a7ee 62%,#1676d4 100%)}
.hero.tormel{background:linear-gradient(180deg,#b9d9ef 0%,#8f8374 30%,#6b5b4d 45%,#4fb0e6 62%,#7ba75c 100%)}
.hero.quarry{background:linear-gradient(180deg,#bcd7e8 0%,#4f7a41 30%,#9fbf72 48%,#2e9ee4 60%,#7c6a55 100%)}
.hero.lisbet{background:linear-gradient(180deg,#5aa9ec 0%,#a9d5f4 30%,#9c8f7e 46%,#2aa4ee 60%,#117bd7 100%)}
.hero.vale{background:linear-gradient(180deg,#8cc7ef 0%,#cfe6f3 28%,#5b7b77 48%,#8b6d52 72%,#6f5844 100%)}

.showcase{height:202px}
.showcase .photo{inset:0}
.showcase.arena .photo{background:linear-gradient(180deg,#3f8fd8 0%,#bfe0f4 30%,#6d8f5a 48%,#4a6a86 64%,#7b6751 78%,#4e8a3a 100%)}
.showcase.hotel .photo{background:linear-gradient(180deg,#a9cfe8 0%,#e7e9ea 35%,#a89f91 55%,#2e9fd9 68%,#4f9a3a 80%,#64ae42 100%)}
</style>
</head>
<body>

<!-- back cover -->
<section class="page cover" style="left:17px">
  <div class="photo" role="img" aria-label="Curved glazed enclosure over a bright blue swimming pool"></div>
  <div class="brand"><i></i>Lagoon Canopy NZ</div>
  <div class="contact-box">
    <h3>Contact Us</h3>
    <p>Toll Free 0508 SHELTERS (748 219)<br>sales@lagooncanopy.co.nz</p>
  </div>
</section>

<!-- front cover -->
<section class="page cover" style="left:194px">
  <div class="photo" role="img" aria-label="View through an arched pool enclosure along the pool"></div>
  <div class="brand"><i></i>Lagoon Canopy NZ</div>
  <div class="title-panel">
    <h1>Lagoon Canopy NZ</h1>
    <p>Catalogue 2018</p>
  </div>
</section>

<!-- contents & about -->
<section class="spread contents">
  <div class="half left">
    <div class="bar">Table of contents</div>
    <ul class="toc">
      <li><span>RIVELLE HORIZON</span><span>5</span></li>
      <li><span>RIVELLE</span><span>7</span></li>
      <li><span>TORMEL, TORMEL CLEAR</span><span>9</span></li>
      <li><span>QUARRY, QUARRY CLEAR</span><span>11</span></li>
      <li><span>LISBET FUTURE, LISBET</span><span>13</span></li>
      <li><span>VALE SHELTERS</span><span>15</span></li>
    </ul>
    <div class="photo toc-photo" role="img" aria-label="Children playing in a pool"></div>
    <div class="toc-side"></div>
    <div class="folio-dark">2 · Table of contents</div>
  </div>
  <div class="half right">
    <div class="bar head">What We Offer</div>
    <div class="offer-text">
      <p>Do you want to extend your swimming season, keep the water clean and warm, lower heating bills and make more use of your pool all year?</p>
      <p>At Lagoon Canopy our main aim is to give you great service from first call to the finished build. We supply quality enclosures at fair prices.</p>
      <p>Our enclosures are easy to install and look great, with no consent needed in most areas. Get in touch for a quote.</p>
    </div>
    <div class="photo swim-photo" role="img" aria-label="Swimmer in a pool"></div>
    <div class="bar adv">Enclosure Advantages</div>
    <div class="adv-box">
      <ul>
        <li>Year-round average of 8 degree warmer water</li>
        <li>Swim all year round</li>
        <li>Protection from wind and bad weather</li>
        <li>Minimal cleaning needed</li>
        <li>Keeps debris out of the pool</li>
        <li>Cut down water evaporation</li>
        <li>Reduce pool maintenance costs</li>
        <li>Increase pool safety</li>
        <li>Private outdoor UV protection</li>
        <li>No ongoing maintenance costs</li>
        <li>Add value to your property</li>
      </ul>
      <div class="photo adv-photo" role="img" aria-label="Enclosed pool with sunlit water"></div>
    </div>
    <div class="folio-dark">What we offer · 3</div>
  </div>
</section>

<!-- Rivelle Horizon -->
<section class="spread product" style="left:17px;top:303px">
  <div class="photo hero horizon" role="img" aria-label="Low enclosure beside a pool with a child jumping in, trees behind"></div>
  <table class="specs" style="top:80px">
    <tr><th>Dimensions of custom made enclosures</th><th>Rivelle Horizon</th></tr>
    <tr><td>Width</td><td>from 3 m to 8 m</td></tr>
    <tr><td>Length</td><td>unlimited</td></tr>
  </table>
  <table class="specs" style="top:100px">
    <tr><th>Dimensions of standard enclosures</th><th>Horizon A</th><th>Horizon B</th></tr>
    <tr><td>Outer width</td><td>590 cm</td><td>640 cm</td></tr>
    <tr><td>Inner width</td><td>550 cm</td><td>600 cm</td></tr>
    <tr><td>Outer height</td><td>75 cm</td><td>75 cm</td></tr>
  </table>
  <div class="headline">
    <h2>Rivelle<br>Horizon</h2>
    <p>If you love clean lines and a low profile, this model blends into any garden. The segments slide easily and stack at one end for open-air swimming on hot days.</p>
  </div>
  <div class="strip">
    <div class="photo thumb t1" role="img" aria-label="Low enclosure over pool"></div>
    <div class="frame">
      <div class="photo thumb t2" role="img" aria-label="Pool enclosure in garden"></div>
      <div class="photo thumb t3" role="img" aria-label="Enclosure beside a house"></div>
    </div>
    <div class="photo thumb t4" role="img" aria-label="Pool with opened enclosure"></div>
  </div>
  <div class="folio l"><b></b>4 · Rivelle Horizon</div>
  <div class="folio r">Rivelle Horizon · 5<b></b></div>
</section>

<!-- Rivelle -->
<section class="spread product" style="left:371px;top:303px">
  <div class="photo hero rivelle" role="img" aria-label="Tall glazed enclosure over a pool with hedges behind"></div>
  <table class="specs" style="top:98px">
    <tr><th>Dimensions of custom made enclosures</th><th>Rivelle</th></tr>
    <tr><td>Width</td><td>from 3 m to 10 m</td></tr>
    <tr><td>Length</td><td>unlimited</td></tr>
  </table>
  <div class="headline">
    <h2>Rivelle</h2>
    <p>A tall classic with room to stand and walk around the pool. Swim in any weather and enjoy a sheltered space for lounging with family and friends.</p>
  </div>
  <div class="strip">
    <div class="photo thumb t3" role="img" aria-label="Tall enclosure side view"></div>
    <div class="frame">
      <div class="photo thumb t2" role="img" aria-label="Enclosure on a lawn"></div>
      <div class="photo thumb t1" role="img" aria-label="Pool inside enclosure"></div>
    </div>
    <div class="photo thumb t4" role="img" aria-label="Enclosure on a terrace"></div>
  </div>
  <div class="folio l"><b></b>6 · Rivelle</div>
  <div class="folio r">Rivelle · 7<b></b></div>
</section>

<!-- Tormel -->
<section class="spread product" style="left:17px;top:530px">
  <div class="photo hero tormel" role="img" aria-label="Modern house with a low pool enclosure and bean bags on the terrace"></div>
  <table class="specs" style="top:86px">
    <tr><th>Dimensions of custom made enclosures</th><th>Tormel Clear</th></tr>
    <tr><td>Width</td><td>from 3 m to 6 m</td></tr>
    <tr><td>Length</td><td>unlimited</td></tr>
  </table>
  <table class="specs" style="top:106px">
    <tr><th>Standard enclosures</th><th>Tormel A</th><th>Tormel B</th><th>Tormel C</th></tr>
    <tr><td>Outer width</td><td>387 cm</td><td>437 cm</td><td>487 cm</td></tr>
    <tr><td>Inner width</td><td>347 cm</td><td>397 cm</td><td>447 cm</td></tr>
    <tr><td>Outer height</td><td>98 cm</td><td>104 cm</td><td>112 cm</td></tr>
  </table>
  <div class="headline">
    <h2>Tormel<br>Tormel Clear</h2>
    <p>A simple, sturdy enclosure at a friendly price. Its rounded shape suits most gardens, and clear panels keep the view open for many years.</p>
  </div>
  <div class="strip">
    <div class="photo thumb t2" role="img" aria-label="House with enclosed pool"></div>
    <div class="frame">
      <div class="photo thumb t1" role="img" aria-label="Pool enclosure from above"></div>
      <div class="photo thumb t4" role="img" aria-label="Enclosure near palms"></div>
    </div>
    <div class="photo thumb t3" role="img" aria-label="Enclosure corner detail"></div>
  </div>
  <div class="folio l"><b></b>8 · Tormel, Tormel Clear</div>
  <div class="folio r">Tormel, Tormel Clear · 9<b></b></div>
</section>

<!-- Quarry -->
<section class="spread product" style="left:371px;top:530px">
  <div class="photo hero quarry" role="img" aria-label="Garden pool with a low enclosure and a deck table in front"></div>
  <table class="specs" style="top:86px">
    <tr><th>Dimensions of custom made enclosures</th><th>Quarry Clear</th></tr>
    <tr><td>Width</td><td>from 3 m to 7 m</td></tr>
    <tr><td>Length</td><td>unlimited</td></tr>
  </table>
  <table class="specs" style="top:106px">
    <tr><th>Standard enclosures</th><th>Quarry A</th><th>Quarry B</th><th>Quarry C</th></tr>
    <tr><td>Outer width</td><td>417 cm</td><td>467 cm</td><td>517 cm</td></tr>
    <tr><td>Inner width</td><td>379 cm</td><td>429 cm</td><td>479 cm</td></tr>
    <tr><td>Outer height</td><td>101 cm</td><td>107 cm</td><td>115 cm</td></tr>
  </table>
  <div class="headline">
    <h2>Quarry<br>Quarry Clear</h2>
    <p>If you want shape and style, this model fits the bill. Low and elegant, it protects your pool while looking at home in any setting.</p>
  </div>
  <div class="strip">
    <div class="photo thumb t4" role="img" aria-label="Enclosure by a house"></div>
    <div class="frame">
      <div class="photo thumb t3" role="img" aria-label="Pool with stone edge"></div>
      <div class="photo thumb t1" role="img" aria-label="Clear enclosure close up"></div>
    </div>
    <div class="photo thumb t2" role="img" aria-label="Enclosure at dusk"></div>
  </div>
  <div class="folio l"><b></b>10 · Quarry, Quarry Clear</div>
  <div class="folio r">Quarry, Quarry Clear · 11<b></b></div>
</section>

<!-- Lisbet -->
<section class="spread product" style="left:17px;top:753px">
  <div class="photo hero lisbet" role="img" aria-label="Arched tall enclosure over a pool beside a brick house"></div>
  <table class="specs" style="top:86px">
    <tr><th>Dimensions of custom made enclosures</th><th>Lisbet Future</th></tr>
    <tr><td>Width</td><td>from 4 m to 9 m</td></tr>
    <tr><td>Length</td><td>unlimited</td></tr>
  </table>
  <table class="specs" style="top:106px">
    <tr><th>Dimensions of custom made enclosures</th><th>Lisbet</th></tr>
    <tr><td>Width</td><td>from 3 m to 8 m</td></tr>
    <tr><td>Length</td><td>unlimited</td></tr>
  </table>
  <div class="headline">
    <h2>Lisbet Future<br>Lisbet</h2>
    <p>A roomy design for those who like space. Both models give an elegant touch to your pool area and are easy to open on warm days.</p>
  </div>
  <div class="strip">
    <div class="photo thumb t3" role="img" aria-label="Tall enclosure side view"></div>
    <div class="frame">
      <div class="photo thumb t1" role="img" aria-label="Pool under arched roof"></div>
      <div class="photo thumb t2" role="img" aria-label="Enclosure on lawn"></div>
    </div>
    <div class="photo thumb t4" role="img" aria-label="Arched enclosure outside"></div>
  </div>
  <div class="folio l"><b></b>12 · Lisbet Future, Lisbet</div>
  <div class="folio r">Lisbet Future, Lisbet · 13<b></b></div>
</section>

<!-- Vale Shelters -->
<section class="spread product" style="left:371px;top:753px">
  <div class="photo hero vale" role="img" aria-label="Tall glass enclosure on a timber deck with trees behind"></div>
  <div class="headline">
    <h2>Vale<br>Shelters</h2>
    <p>We also offer many other enclosure types, from spa covers to walls and roofs for larger pools. Ask us about a custom solution.</p>
  </div>
  <div class="strip">
    <div class="photo thumb t2" role="img" aria-label="Enclosure by a pond"></div>
    <div class="frame">
      <div class="photo thumb t1" role="img" aria-label="Spa enclosure"></div>
      <div class="photo thumb t3" role="img" aria-label="Enclosure with panels opened"></div>
    </div>
    <div class="photo thumb t4" role="img" aria-label="Enclosure on tiled deck"></div>
  </div>
  <div class="folio l"><b></b>14 · Vale Shelters</div>
  <div class="folio r">Vale Shelters · 15<b></b></div>
</section>

<!-- commercial -->
<section class="spread showcase arena" style="left:17px;top:977px">
  <div class="photo" role="img" aria-label="Large commercial enclosure over a pool on a wide timber deck"></div>
</section>
<section class="spread showcase hotel" style="left:371px;top:977px">
  <div class="photo" role="img" aria-label="Commercial pool enclosure in front of a hotel with a lawn"></div>
</section>

</body>
</html>
```